Flyer für Fußball-Feriencamps
Unglaublich tolle Arbeit - Vielen herzlichen Dank!
Zielgruppe
Die TRV-Academy ist eine unabhängige, junge und aufstrebende Akademie.
Wir entwickeln junge Spieler von U9 bis U19 in den bereichen Persönlichkeit, Mentale stärke und das Fußballerische Talent. Wir bieten Modernste und einzigartige Methoden sowie Konzepte.
Aufgabenstellung
Wir benötigen einen einheitlichen Flyer für alle unsere Fußball-Feriencamps.
Da wir mit verschiedenen Fußballvereinen Arbeiten, wäre es wichtig das es ein freies Feld gibt, wo wir dann im nachhinein die Termine drüber legen können.
Unser TRV Logo sollte auf den Flyer
In der Anlage ist ein Beispiel unseres alten Flyer als Beispiel in welche Richtung es gehe könnte.
Wir freuen uns auf kreative und innovative Ideen. :-)
folgende Begriffe sollten vorkommen: Koordination - Schnelligkeit - Technik - Spielintelligenz - Fitness
sowie: Mentale Leistungsfähigkeit - Selbstbewusstsein - Motivation - Soziale Kompetenzen
(Vielleicht auch in Pyramiden dargestellt?)
+ Training mit Modernsten Methoden und einzigartigen Technologien
Toll wäre auch, wenn folgendes irgendwo auftauchen würde: Konzentration verbessern - Motivation erhöhen - Mentale Leistung steigern - Selbstvertrauen stärken - Disziplin verbessern und mehr.
ganz unten vielleicht dann: Infos & Anmeldung unter: www.trv-academy.de

```html
<!DOCTYPE html>
<html lang="de">
<head>
<meta charset="utf-8">
<title>Fußball Feriencamp – TRV-Academy</title>
<link href="https://fonts.googleapis.com/css2?family=Source+Sans+3:ital,wght@0,300;0,400;0,600;0,700;1,400&display=swap" rel="stylesheet">
<style>
  :root {
    --backdrop: #a0a09e;
    --paper: #ffffff;
    --ink: #141414;
    --teal: #2a6e87;
    --date-field: #e1e8eb;
    --photo-sky: #6c7c80;
    --photo-mid: #56707a;
    --grass-light: #7fa45c;
    --grass: #5e8a3a;
    --badge: #1c1c1c;
  }
  * { margin: 0; padding: 0; box-sizing: border-box; }
  html, body { width: 900px; height: 1200px; overflow: hidden; }
  body {
    background: var(--backdrop);
    font-family: "Source Sans 3", sans-serif;
    color: var(--ink);
    position: relative;
  }
  .flyer {
    position: absolute; left: 135px; top: 153px;
    width: 629px; height: 893px;
    background: var(--paper);
  }
  .hero-photo {
    position: absolute; left: 22px; top: 22px; width: 586px; height: 338px;
    background: linear-gradient(180deg, var(--photo-sky) 0%, var(--photo-mid) 55%, var(--grass-light) 82%, var(--grass) 100%);
  }
  .footer-photo {
    position: absolute; left: 22px; top: 761px; width: 586px; height: 110px;
    background: linear-gradient(180deg, var(--grass-light) 0%, var(--grass) 100%);
  }
  .brand {
    position: absolute; left: 485px; top: 30px; width: 104px; height: 104px;
    border-radius: 50%; background: var(--badge);
    display: flex; align-items: center; justify-content: center; text-align: center;
    color: #fff; font-weight: 700; font-size: 17px; line-height: 1.05;
  }
  .title-main {
    position: absolute; left: 348px; top: 302px;
    color: #fff; font-weight: 700; font-size: 50px; letter-spacing: 1px; line-height: 1;
  }
  .title-sub {
    position: absolute; left: 347px; top: 364px;
    color: var(--teal); font-weight: 300; font-size: 46px; line-height: 1; letter-spacing: 0.5px;
  }
  .headline {
    position: absolute; left: 22px; top: 383px; width: 330px;
    font-weight: 600; font-size: 31.5px; line-height: 37.8px;
  }
  .headline em { font-style: normal; font-weight: 700; color: var(--teal); }
  .skills {
    position: absolute; left: 22px; top: 589px;
    font-size: 17.5px; line-height: 22px;
  }
  .date-field {
    position: absolute; left: 22px; top: 648px; width: 284px; height: 97px;
    background: var(--date-field);
  }
  .right-col { position: absolute; left: 351px; top: 416px; width: 260px; }
  .claim { font-weight: 700; font-size: 18.5px; line-height: 24px; }
  .benefits { list-style: none; font-size: 17.3px; line-height: 21.6px; margin-top: 6px; }
  .benefits + .benefits { margin-top: 11px; }
  .benefits li::before { content: "• "; }
  .signup { margin-top: 16px; color: var(--teal); font-size: 17.3px; line-height: 17px; }
  .signup strong { font-weight: 600; display: block; }
  .signup a { color: inherit; text-decoration: none; font-style: italic; }
</style>
</head>
<body>
  <div class="flyer">
    <div class="hero-photo" role="img" aria-label="Foto: Fußball im Tornetz vor unscharfem Stadionhintergrund"></div>
    <div class="brand">TRV<br>Academy</div>
    <div class="title-main">FUSSBALL</div>
    <div class="title-sub">FERIENCAMP</div>

    <h1 class="headline">Der Weg einer<br>sinnvollen Förderung<br>im <em>Fußball</em> und<br>zugleich für <em>Schule</em><br>und <em>Leben!</em></h1>
    <p class="skills">Koordination | Schnelligkeit<br>Technik | Spielintelligenz | Fitness</p>
    <div class="date-field" aria-label="Freies Feld für Termine"></div>

    <div class="right-col">
      <p class="claim">Training mit Modernsten Methoden und einzigartigen Technologien</p>
      <ul class="benefits">
        <li>Konzentration verbessern</li>
        <li>Motivation erhöhen</li>
        <li>Mentale Leistung steigern</li>
        <li>Selbstvertrauen stärken</li>
        <li>Disziplin verbessern</li>
      </ul>
      <ul class="benefits">
        <li>Mentale Leistungsfähigkeit</li>
        <li>Selbstbewusstsein</li>
        <li>Motivation</li>
        <li>Soziale Kompetenzen</li>
      </ul>
      <p class="signup"><strong>Infos &amp; Anmeldung unter:</strong><a href="#">www.trv-academy.de</a></p>
    </div>

    <div class="footer-photo" role="img" aria-label="Foto: Fußball im Netz über grünem Rasen"></div>
  </div>
</body>
</html>
```